Business brochure/booklet design

Good days,
We want to have a new design of the company brochure. The idea and content is already described in the attached draft.
The brochure is a booklet, size of each page is about 21 x 28.5cm.
There are some pictures in the draft which are for you to understand our concept and preference. You can replace them (except company logo and diagram, product pictures) to better meet the concept or the overall design.
Thank you!

```html
<!DOCTYPE html>
<html lang="en">
<head>
<meta charset="utf-8">
<title>Verdant Farms – Company Brochure</title>
<link href="https://fonts.googleapis.com/css2?family=Cormorant+Garamond:wght@500;600&family=Montserrat:wght@400;500;600;700&display=swap" rel="stylesheet">
<style>
  :root {
    --green: #1f9a4b;
    --green-dark: #137a37;
    --green-light: #5cbf73;
    --ink: #333a36;
    --muted: #7c837f;
    --paper: #ffffff;
    --backdrop: #e8e9e8;
    --rule: #d9dcda;
  }
  * { box-sizing: border-box; margin: 0; padding: 0; }
  html, body { width: 1200px; height: 3000px; overflow: hidden; }
  body { background: var(--backdrop); font-family: "Montserrat", sans-serif; color: var(--ink); position: relative; }

  .page { position: absolute; width: 442px; height: 600px; background: var(--paper); overflow: hidden; box-shadow: 0 6px 18px rgba(0,0,0,.12); }
  .spread { position: absolute; left: 158px; width: 884px; height: 600px; box-shadow: 0 6px 18px rgba(0,0,0,.12); }
  .spread .page { top: 0; box-shadow: none; }
  .spread .left { left: 0; }
  .spread .right { left: 442px; border-left: 1px solid var(--rule); }

  .photo { position: absolute; }

  /* Cover */
  .cover { left: 379px; top: 100px; }
  .cover .disc { position: absolute; width: 420px; height: 420px; border-radius: 50%; background: var(--green); left: 120px; top: -70px; }
  .cover .ring { position: absolute; width: 470px; height: 470px; border-radius: 50%; border: 3px solid var(--green-light); left: 96px; top: -96px; }
  .cover-title { position: absolute; left: 156px; top: 78px; font-family: "Cormorant Garamond", serif; font-weight: 600; font-size: 36px; line-height: 1.08; color: #fff; letter-spacing: 1px; }
  .cover-title span { display: block; }
  .brand { position: absolute; display: flex; align-items: center; gap: 6px; font-weight: 700; font-size: 12px; color: var(--green); }
  .brand .mark { width: 14px; height: 14px; background: var(--green); border-radius: 50%; }
  .cover .brand { right: 24px; top: 22px; color: #fff; }
  .cover .brand .mark { background: #fff; }
  .features { position: absolute; left: 40px; top: 400px; display: flex; gap: 46px; }
  .feature { width: 80px; text-align: center; font-size: 9px; font-weight: 600; color: var(--ink); }
  .feature .icon { width: 46px; height: 46px; margin: 0 auto 8px; border-radius: 50%; background: #2b2f2d; display: flex; align-items: center; justify-content: center; }
  .cover-foot { position: absolute; left: 0; bottom: 30px; width: 100%; height: 40px; }
  .cover-foot .band { position: absolute; left: 0; top: 0; width: 300px; height: 40px; background: var(--green); clip-path: polygon(0 0, 100% 0, 88% 100%, 0 100%); }
  .cover-foot .email { position: absolute; left: 40px; top: 13px; color: #fff; font-size: 11px; font-weight: 500; }
  .cover-foot .stripe { position: absolute; top: 0; height: 40px; width: 28px; background: var(--green-light); transform: skewX(-20deg); }

  /* Contents */
  .contents-spread { top: 820px; }
  .contents-photo { left: -130px; top: 40px; width: 520px; height: 520px; border-radius: 50%; background: linear-gradient(180deg, #6fa7d8 0%, #a9c9e6 45%, #8a8f88 70%, #5a6b7a 100%); }
  .contents-title { position: absolute; left: 50px; top: 70px; writing-mode: vertical-rl; text-orientation: upright; font-weight: 600; font-size: 22px; letter-spacing: 2px; color: var(--green); }
  .toc { position: absolute; left: 110px; top: 80px; width: 280px; list-style: none; font-size: 11px; line-height: 1.4; }
  .toc li { display: flex; justify-content: space-between; gap: 16px; margin-bottom: 16px; color: var(--ink); }
  .toc .num { color: var(--green); font-weight: 600; }
  .toc-rule { position: absolute; left: 90px; top: 70px; width: 2px; height: 240px; background: var(--green-light); }

  /* Company profile */
  .profile-spread { top: 1540px; }
  .profile-photo { left: -90px; top: 40px; width: 500px; height: 500px; border-radius: 50%; background: linear-gradient(160deg, #7fb2dc 0%, #b7d3e8 40%, #4f8a3d 62%, #2f6b2b 100%); }
  .profile-accent { position: absolute; left: 160px; top: 290px; width: 260px; height: 260px; border-radius: 0 0 260px 0; background: var(--green); opacity: .85; }
  .tag { position: absolute; left: 30px; top: 40px; background: var(--green); color: #fff; font-size: 12px; font-weight: 700; letter-spacing: 1px; padding: 9px 34px 9px 16px; clip-path: polygon(0 0, 100% 0, 92% 100%, 0 100%); }
  .body-copy { position: absolute; left: 30px; width: 290px; }
  .body-copy h3 { font-size: 11px; color: var(--green); font-weight: 700; margin: 18px 0 6px; text-transform: uppercase; }
  .body-copy p { font-size: 9.5px; line-height: 1.6; color: var(--muted); }
  .profile-strip { right: 0; top: 90px; width: 100px; height: 510px; background: linear-gradient(180deg, #9a9d9b 0%, #6d716e 60%, #4d514e 100%); }

  /* Products */
  .products-spread { top: 2260px; }
  .products-photo { left: 0; top: 0; width: 442px; height: 300px; background: linear-gradient(135deg, #6aa84f 0%, #c0392b 45%, #8fbf5a 75%, #3e6b2f 100%); }
  .products-band { position: absolute; left: 0; top: 300px; width: 330px; height: 60px; background: var(--green); clip-path: polygon(0 0, 100% 0, 90% 100%, 0 100%); color: #fff; padding: 14px 24px; }
  .products-band h2 { font-size: 15px; font-weight: 700; letter-spacing: .5px; }
  .products-band p { font-size: 9px; margin-top: 2px; }
  .product-row { position: absolute; left: 30px; top: 400px; display: flex; gap: 22px; }
  .product { width: 84px; text-align: center; font-size: 9px; color: var(--ink); font-weight: 600; }
  .product .dish { width: 74px; height: 74px; margin: 0 auto 8px; border-radius: 50%; background: radial-gradient(circle, #d9a441 0%, #a9742a 70%, #6e4a1d 100%); }
  .products-spread .right .tag { left: 30px; top: 36px; }
  .app-photo { right: -40px; bottom: -40px; width: 360px; height: 320px; border-radius: 50% 0 0 0; background: linear-gradient(150deg, #cfe8d4 0%, #7cc08a 45%, #2f8a4a 100%); }
</style>
</head>
<body>

  <section class="page cover">
    <div class="ring"></div>
    <div class="disc"></div>
    <div class="brand"><span class="mark"></span>Verdant Farms</div>
    <h1 class="cover-title">
      <span>FARMING</span>
      <span>INTELLIGENT</span>
      <span>TECHNOLOGY</span>
    </h1>
    <div class="features">
      <div class="feature">
        <div class="icon"><svg width="22" height="22" viewBox="0 0 24 24" fill="none" stroke="#fff" stroke-width="2"><rect x="4" y="3" width="16" height="18" rx="2"/><path d="M8 8h8M8 12h8M8 16h5"/></svg></div>
        Smart Records
      </div>
      <div class="feature">
        <div class="icon"><svg width="22" height="22" viewBox="0 0 24 24" fill="none" stroke="#fff" stroke-width="2"><circle cx="12" cy="12" r="8"/><path d="M8 12l3 3 5-6"/></svg></div>
        Quality Check
      </div>
      <div class="feature">
        <div class="icon"><svg width="22" height="22" viewBox="0 0 24 24" fill="none" stroke="#fff" stroke-width="2"><rect x="7" y="2" width="10" height="20" rx="2"/><path d="M11 18h2"/></svg></div>
        Mobile Tracking
      </div>
    </div>
    <div class="cover-foot">
      <div class="band"></div>
      <span class="email">hello@verdantfarms.example</span>
      <span class="stripe" style="left:312px"></span>
      <span class="stripe" style="left:350px"></span>
      <span class="stripe" style="left:388px"></span>
      <span class="stripe" style="left:426px"></span>
    </div>
  </section>

  <section class="spread contents-spread">
    <div class="page left">
      <div class="photo contents-photo" role="img" aria-label="City waterfront skyline with a landmark statue and domed buildings"></div>
    </div>
    <div class="page right">
      <h2 class="contents-title">CONTENT</h2>
      <div class="toc-rule"></div>
      <ol class="toc">
        <li><span>About Verdant Farms</span><span class="num">1</span></li>
        <li><span>IoT – Farming Intelligent Technology</span><span class="num">3</span></li>
        <li><span>IoT Supply Chain Business Transformation</span><span class="num">5</span></li>
        <li><span>IoT Business Development</span><span class="num">7</span></li>
        <li><span>Verdant Tag App</span><span class="num">11</span></li>
      </ol>
    </div>
  </section>

  <section class="spread profile-spread">
    <div class="page left">
      <div class="photo profile-photo" role="img" aria-label="City landmark beside green terraced rice fields"></div>
      <div class="profile-accent"></div>
    </div>
    <div class="page right">
      <div class="tag">COMPANY PROFILE</div>
      <div class="body-copy" style="top:80px">
        <h3>Our Vision</h3>
        <p>To bring smart, sustainable farming to every grower through connected tools and honest data.</p>
        <h3>Our Mission</h3>
        <p>We build sensor networks and simple apps that help farms grow more food with less water, less waste and full traceability from field to table.</p>
        <h3>Who We Are</h3>
        <p>Verdant Farms is a team of agronomists and engineers working with growers across the region. We design, install and support intelligent farming systems that turn daily field readings into clear actions, helping partners raise yields and meet rising standards for quality.</p>
      </div>
      <div class="photo profile-strip" role="img" aria-label="Aerial view of farmland in greyscale"></div>
    </div>
  </section>

  <section class="spread products-spread">
    <div class="page left">
      <div class="photo products-photo" role="img" aria-label="Hand holding a phone in front of fresh produce at a market"></div>
      <div class="products-band">
        <h2>OUR PRODUCTS</h2>
        <p>Fresh, traceable and grown smart</p>
      </div>
      <div class="product-row">
        <div class="product"><div class="dish" role="img" aria-label="Prepared dish"></div>Rice Bowl</div>
        <div class="product"><div class="dish" role="img" aria-label="Prepared dish"></div>Noodles</div>
        <div class="product"><div class="dish" role="img" aria-label="Prepared dish"></div>Dumplings</div>
        <div class="product"><div class="dish" role="img" aria-label="Prepared dish"></div>Greens</div>
      </div>
    </div>
    <div class="page right">
      <div class="tag">VERDANT TAG APP</div>
      <div class="body-copy" style="top:76px; width:380px">
        <p>Verdant Tag links every harvest to a simple code. Buyers scan it with a phone to see where the produce grew, when it was picked and how it was handled on the way to them.</p>
        <p style="margin-top:10px">Growers use the same app to log tasks, watch sensor alerts and share records with partners in seconds, keeping the whole chain clear and trusted.</p>
      </div>
      <div class="photo app-photo" role="img" aria-label="Hands holding a phone showing the app above fresh leafy greens"></div>
    </div>
  </section>

</body>
</html>
```